Letter Head Design - Finance industry

Design a letterhead to match the logo. Needs to be clean, simple and crisp. I'm open to suggestions. Will be using the logo that was submitted last with the W crossed over

Target Market(s)

Small medium businesses and government department's

Industry/Entity Type

Industry

Font styles to use
Sans Serif

Colors
cadf82
bcd85c
acd036
9bcb3c
e9e9e9
aaaaaa
000000
7f7f7f
b7b7b7

Requirements
Must have
• Need to display: Logo, Business address, ABN number, ASIC register number, contact phone, website, company email. Details are as per below:

Suite 4B Level 17
Marlowe Crest House
9 Tindall Lane
Sydney NSW 2000
Landline Ph: 02 5193 4620
Ph: 1300 4719 55
Email: enquiries@coinharbourco.com.au
W: www.coinharbourco.com.au

On the footer, the details below need to be specified:
ABN: 47 381 950 623
ASIC Registration Number: 31 749218605

Should not have
• No imagery or design that is not in line with the logo

```html
<!DOCTYPE html>
<html lang="en">
<head>
<meta charset="utf-8">
<title>Coin Harbour — Letterhead</title>
<link href="https://fonts.googleapis.com/css2?family=Lato:wght@300;400&display=swap" rel="stylesheet">
<style>
  :root {
    --green: #9bcb3c;
    --green-light: #acd036;
    --grey-mid: #aaaaaa;
    --grey-dark: #7f7f7f;
    --grey-soft: #b7b7b7;
    --grey-pale: #e9e9e9;
    --ink: #222222;
    --white: #ffffff;
  }
  * { margin: 0; padding: 0; box-sizing: border-box; }
  html, body { width: 883px; height: 1200px; overflow: hidden; background: var(--white); }
  .letterhead {
    position: relative;
    width: 883px;
    height: 1200px;
    font-family: "Lato", sans-serif;
    color: var(--ink);
    overflow: hidden;
  }
  .header-swoosh { position: absolute; top: 0; left: 0; }
  .brand {
    position: absolute;
    left: 20px;
    top: 30px;
    display: flex;
    align-items: center;
    gap: 16px;
  }
  .brand-mark {
    width: 76px;
    height: 76px;
    border-radius: 50%;
    background: var(--green);
  }
  .brand-name {
    font-family: "Lato", sans-serif;
    font-weight: 400;
    font-size: 46px;
    line-height: 45px;
    color: var(--grey-dark);
  }
  .contact {
    position: absolute;
    right: 26px;
    top: 10px;
    list-style: none;
    text-align: right;
    color: var(--white);
    font-size: 12.5px;
    font-weight: 300;
    letter-spacing: 0.2px;
  }
  .contact li {
    display: flex;
    justify-content: flex-end;
    align-items: center;
    gap: 7px;
    height: 14.2px;
  }
  .contact li.gap { margin-top: 2px; height: 15.5px; }
  .contact .icon { width: 10px; height: 10px; flex: none; }
  .contact .icon-blank { width: 10px; flex: none; }
  .salutation {
    position: absolute;
    left: 98px;
    top: 305px;
    font-size: 20px;
    font-weight: 400;
  }
  .body-copy {
    position: absolute;
    left: 98px;
    top: 380px;
    width: 653px;
    font-size: 15.6px;
    font-weight: 300;
    line-height: 23.8px;
    text-align: justify;
    hyphens: auto;
  }
  .body-copy p + p { margin-top: 23.8px; }
  .sign-off { position: absolute; left: 98px; top: 805px; }
  .signer-name { font-size: 20px; font-weight: 400; }
  .signer-role { font-size: 13.5px; font-weight: 300; margin-top: 6px; }
  .signature {
    position: absolute;
    left: 78px;
    top: 910px;
    width: 174px;
    height: 74px;
    background: var(--grey-pale);
    border-radius: 4px;
  }
  .footer-rule {
    position: absolute;
    left: 26px;
    top: 1127px;
    width: 817px;
    height: 1.5px;
    background: var(--green);
  }
  .footer-details {
    position: absolute;
    left: 0;
    top: 1139px;
    width: 866px;
    text-align: center;
    color: var(--grey-mid);
    font-size: 13px;
    line-height: 17px;
  }
</style>
</head>
<body>
<main class="letterhead">
  <svg class="header-swoosh" width="883" height="170" viewBox="0 0 883 170" aria-hidden="true">
    <path d="M138,0 C300,30 420,122 600,142 C700,152 800,154 883,154 L883,160 C800,160 700,158 600,148 C420,128 300,34 138,0 Z" fill="var(--grey-pale)"/>
    <path d="M138,0 C300,30 420,116 600,136 C700,146 800,148 883,148 L883,154 C800,154 700,152 600,142 C420,122 300,32 138,0 Z" fill="var(--grey-soft)"/>
    <path d="M138,0 L883,0 L883,142 C800,142 700,140 600,130 C420,110 300,28 138,0 Z" fill="var(--green)"/>
  </svg>

  <div class="brand">
    <span class="brand-mark"></span>
    <span class="brand-name">Coin<br>Harbour</span>
  </div>

  <ul class="contact">
    <li>Suite 4B Level 17
      <svg class="icon" viewBox="0 0 10 10"><path d="M5 0.5a3 3 0 0 1 3 3c0 2.2-3 6-3 6s-3-3.8-3-6a3 3 0 0 1 3-3z" fill="var(--white)"/><circle cx="5" cy="3.5" r="1.1" fill="var(--green)"/></svg></li>
    <li>Marlowe Crest House<span class="icon-blank"></span></li>
    <li>9 Tindall Lane<span class="icon-blank"></span></li>
    <li>Sydney NSW 2000<span class="icon-blank"></span></li>
    <li class="gap">02 5193 4620
      <svg class="icon" viewBox="0 0 10 10"><rect x="1" y="1" width="8" height="8" rx="1" fill="var(--white)"/><rect x="2.5" y="2.5" width="2" height="5" fill="var(--green)"/></svg></li>
    <li class="gap">1300 4719 55
      <svg class="icon" viewBox="0 0 10 10"><rect x="2.5" y="0.5" width="5" height="9" rx="1" fill="var(--white)"/><rect x="3.5" y="1.8" width="3" height="5" fill="var(--green)"/></svg></li>
    <li class="gap">enquiries@coinharbourco.com.au
      <svg class="icon" viewBox="0 0 10 10"><rect x="0.5" y="2" width="9" height="6" fill="var(--white)"/><path d="M0.5 2 L5 5.5 L9.5 2" stroke="var(--green)" fill="none"/></svg></li>
    <li>www.coinharbourco.com.au
      <svg class="icon" viewBox="0 0 10 10"><circle cx="5" cy="5" r="4.3" fill="none" stroke="var(--white)" stroke-width="1.2"/><path d="M1 5h8M5 1c-2 2.5-2 5.5 0 8M5 1c2 2.5 2 5.5 0 8" stroke="var(--white)" fill="none" stroke-width="0.8"/></svg></li>
  </ul>

  <p class="salutation">Dear Mr. Hartley,</p>

  <section class="body-copy">
    <p>Lorem ipsum dolor sit amet, consectetur adipiscing elit. Donec orci purus, luctus vitae dignissim eu, iaculis sed purus. Vivamus faucibus, ipsum nec aliquet viverra, leo mauris condimentum ligula, sit amet sagittis enim ligula quis arcu. Nam egestas tortor id nisi porttitor mattis. In tortor ante, ultricies in suscipit a, tempus non massa. Vivamus et auctor mi. Fusce vel massa nulla. Phasellus nec eros mauris, et scelerisque orci. Donec malesuada orci vitae nulla accumsan porta a id massa. Quisque accumsan iaculis magna sit amet fringilla. Maecenas consequat, magna eget tincidunt semper, odio nibh rutrum mi, id feugiat ante nisi eu risus. Vestibulum nunc orci, rhoncus a placerat in, ultricies in mi. Cras mattis varius eros, vel fringilla nisi suscipit eget.</p>
    <p>Quisque scelerisque sagittis nulla at porttitor. Mauris a justo et tellus interdum tristique. Sed id augue vitae urna euismod commodo aliquet a quam. Pellentesque arcu velit, cursus et malesuada ut, consequat et diam. Nullam erat sem, rhoncus id ullamcorper vitae, rhoncus et arcu. In ultricies ultricies nulla, ut rutrum nisi iaculis at. Donec eu magna a metus ornare faucibus. Fusce aliquet faucibus ultricies. Morbi semper, est id tincidunt gravida, sem arcu adipiscing lacus, ac bibendum nulla leo eu purus. Quisque nec diam sed risus consectetur a ccumsan quis quis nibh. Vestibulum id purus lorem.</p>
  </section>

  <div class="sign-off">
    <p class="signer-name">Daniel Marsh</p>
    <p class="signer-role">Co-Founder &amp; CEO</p>
  </div>

  <div class="signature" role="img" aria-label="Handwritten signature of the sender"></div>

  <div class="footer-rule"></div>
  <footer class="footer-details">
    <p>ABN: 47 381 950 623</p>
    <p>ASIC Registration Number: 31 749218605</p>
  </footer>
</main>
</body>
</html>
```